Corwyns Best 4 years in a row

I need a billboard that has all the attached logos and says:

Corwyn's Best Realtor 4 Years in a row!

1.75 Listing Fee

Tobias Wrenfield

555-214-7390

and somewhere very small at the bottom:

855-555-0142

2748 W Amberlow Rd, Larkmoor, EV 20957

I put in the last winner just to give an idea of what I'm looking for, although I'd like to switch it up a little bit.

```html
<!DOCTYPE html>
<html lang="en">
<head>
<meta charset="utf-8">
<title>Tobias Wrenfield Billboard</title>
<link rel="stylesheet" href="https://fonts.googleapis.com/css2?family=Bebas+Neue&family=Montserrat:wght@400;500;700;800&display=swap">
<style>
  :root {
    --stage: #0e1320;
    --paper: #ffffff;
    --navy: #0b2a66;
    --navy-deep: #142c6e;
    --ocean: #1a86c8;
    --sky: #0a8fd6;
    --ice: #d3f3fc;
    --steel: #a9b7c0;
    --grey-text: #5e5e60;
    --badge: #2b2b2d;
  }
  html, body {
    margin: 0;
    padding: 0;
    width: 1200px;
    height: 1200px;
    overflow: hidden;
    background: var(--stage);
  }
  .stage {
    width: 1200px;
    height: 1200px;
    display: flex;
    align-items: center;
    justify-content: center;
  }
  .billboard {
    width: 1140px;
    height: auto;
    display: block;
  }
  .brand-name { font-family: "Montserrat", sans-serif; font-weight: 700; fill: var(--navy); }
  .agent-name { font-family: "Bebas Neue", sans-serif; fill: var(--navy); }
  .tagline { font-family: "Bebas Neue", sans-serif; fill: var(--grey-text); }
  .call-label { font-family: "Bebas Neue", sans-serif; fill: var(--paper); }
  .call-number { font-family: "Montserrat", sans-serif; font-weight: 800; fill: var(--paper); }
  .role-main { font-family: "Montserrat", sans-serif; font-weight: 800; fill: var(--navy); }
  .role-sub { font-family: "Montserrat", sans-serif; font-weight: 400; fill: var(--navy); letter-spacing: 4px; }
  .fee { font-family: "Bebas Neue", sans-serif; fill: var(--paper); }
  .details { font-family: "Montserrat", sans-serif; font-weight: 500; fill: var(--navy); }
</style>
</head>
<body>
<main class="stage">
  <svg class="billboard" viewBox="0 0 1610 468" xmlns="http://www.w3.org/2000/svg">
    <defs>
      <linearGradient id="callBand" x1="0" y1="0" x2="1" y2="0">
        <stop offset="0" stop-color="#14306f"/>
        <stop offset="0.6" stop-color="#155e99"/>
        <stop offset="1" stop-color="#0f9ad0"/>
      </linearGradient>
      <linearGradient id="cornerBlue" x1="0" y1="0" x2="1" y2="0">
        <stop offset="0" stop-color="#16c3e6"/>
        <stop offset="0.5" stop-color="#1378c2"/>
        <stop offset="1" stop-color="#123a86"/>
      </linearGradient>
      <linearGradient id="portraitTone" x1="0" y1="0" x2="0" y2="1">
        <stop offset="0" stop-color="#b9907c"/>
        <stop offset="0.32" stop-color="#d9dce6"/>
        <stop offset="0.5" stop-color="#2a3446"/>
        <stop offset="1" stop-color="#1f2838"/>
      </linearGradient>
    </defs>

    <rect class="sheet" x="0" y="0" width="1610" height="468" fill="var(--paper)"/>

    <g class="brand">
      <circle cx="160" cy="110" r="14" fill="var(--navy)"/>
      <text class="brand-name" x="160" y="170" font-size="26" text-anchor="middle">NORTHGATE TEAM</text>
    </g>

    <polygon class="award-badge" fill="var(--badge)"
      points="397,40 425,50 455,52 466,80 480,105 466,130 455,158 425,160 397,170 369,160 339,158 328,130 314,105 328,80 339,52 369,50"/>

    <text class="agent-name" x="530" y="148" font-size="150" textLength="700" lengthAdjust="spacingAndGlyphs">TOBIAS WRENFIELD</text>
    <text class="tagline" x="530" y="218" font-size="56" textLength="706" lengthAdjust="spacingAndGlyphs">CORWYN'S BEST REALTOR 4 YEARS IN A ROW!</text>

    <rect class="role-rule" x="54" y="282" width="3" height="66" fill="var(--navy)"/>
    <text class="role-main" x="70" y="312" font-size="38">REAL ESTATE</text>
    <text class="role-sub" x="70" y="346" font-size="28">PROFESSIONAL</text>

    <rect class="detail-band" x="0" y="370" width="1400" height="98" fill="var(--ice)"/>
    <polygon class="call-band" points="490,262 1400,262 1400,370 420,370" fill="url(#callBand)"/>
    <polygon class="fee-band" points="0,370 420,370 375,440 0,440" fill="var(--sky)"/>

    <text class="call-label" x="498" y="340" font-size="46">CALL/TEXT</text>
    <text class="call-number" x="690" y="345" font-size="78" textLength="545" lengthAdjust="spacingAndGlyphs">555-214-7390</text>

    <text class="fee" x="52" y="425" font-size="52">1,75% LISTING FEE</text>
    <text class="details" x="450" y="418" font-size="26" textLength="190" lengthAdjust="spacingAndGlyphs">855-555-0142</text>
    <rect class="details-divider" x="663" y="398" width="3" height="22" fill="var(--navy)"/>
    <text class="details" x="690" y="418" font-size="26" textLength="545" lengthAdjust="spacingAndGlyphs">2748 W Amberlow Rd, Larkmoor, EV 20957</text>

    <polygon class="stripe-steel" points="1500,0 1545,0 1285,468 1232,468" fill="var(--steel)"/>
    <polygon class="stripe-blue" points="1545,0 1610,0 1610,468 1285,468" fill="url(#cornerBlue)"/>

    <path class="portrait" role="img" aria-label="Portrait photo of the realtor in a navy suit and white shirt"
      d="M1360,130 Q1360,22 1405,22 Q1450,22 1450,130 L1560,170 Q1592,190 1592,300 L1592,468 L1268,468 L1268,300 Q1268,190 1300,170 Z"
      fill="url(#portraitTone)"/>
  </svg>
</main>
</body>
</html>
```